Pellwick Movers Pre-Mover Postcard

We have created a front and back design through canva.com. It's not bad, but we want a great design. Attached is what we have come up with so far. We want all of the content sections grouped similarly, but want a creative design. It's all in the details.

```html
<!DOCTYPE html>
<html lang="en">
<head>
<meta charset="utf-8">
<title>Pellwick Movers Pre-Mover Postcard</title>
<link href="https://fonts.googleapis.com/css2?family=Source+Sans+3:ital,wght@0,400;0,600;0,700;1,300;1,400&family=Ubuntu:wght@500;700&display=swap" rel="stylesheet">
<style>
:root{
  --navy:#0c2d55;
  --yellow:#f6d30f;
  --white:#ffffff;
  --badge:#2c4a70;
}
*{margin:0;padding:0;box-sizing:border-box}
html,body{width:1200px;height:1200px;overflow:hidden;background:var(--white)}
body{position:relative;font-family:"Source Sans 3",sans-serif;color:var(--navy)}
.abs{position:absolute}
.center{text-align:center}

/* front */
.front{left:0;top:442px;width:571px;height:316px}
.front-photo{left:0;top:0;width:571px;height:105px;
  background:linear-gradient(90deg,#7d8590 0%,#e8eaee 18%,#3a66c4 35%,#eef0f3 55%,#3b67c5 70%,#d9dcdf 85%,#8c8f93 100%)}
.front-notch{left:491px;top:0;width:65px;height:34px;background:var(--white)}
.front-panel{left:58px;top:83px;width:454px;height:91px;background:var(--navy)}
.front-claim{left:0;top:8px;width:454px;color:var(--yellow);font-weight:600;font-size:17px}
.services{left:0;top:60px;width:454px;display:flex;justify-content:space-around;color:var(--yellow);font-weight:600;font-size:11.5px;padding:0 10px}
.front-title{left:0;top:188px;width:571px;font-weight:600;font-size:26px}
.front-sub{left:0;top:224px;width:571px;font-style:italic;font-weight:300;font-size:16px;letter-spacing:.3px}
.front-band{left:0;top:264px;width:571px;height:51px;background:var(--navy);color:var(--white);font-family:"Ubuntu",sans-serif;font-weight:500;font-size:12.5px;letter-spacing:1px;line-height:15.5px;padding-top:10px}

/* back */
.back{left:629px;top:442px;width:571px;height:316px}
.plan{left:0;top:0;width:288px;height:264px}
.plan h2{font-weight:600;font-size:15.5px;margin-top:6px;margin-bottom:8px}
.benefits{list-style:none;font-weight:600;font-size:11.3px;line-height:15.8px}
.stage-title{font-family:"Ubuntu",sans-serif;font-weight:700;font-size:14px;letter-spacing:.3px;line-height:17px}
.stage-body{font-weight:600;font-size:9.8px;line-height:11.3px}
.stage-body.loose{line-height:14px}
.stage1{left:0;top:120px;width:288px}
.stage2{left:0;top:182px;width:288px}

.strategy{left:288px;top:0;width:283px;height:264px;overflow:hidden}
.strategy-photo{left:0;top:0;width:283px;height:264px;
  background:linear-gradient(160deg,#6f7d6a 0%,#9aa3a8 35%,#8b2a2a 55%,#6e7b55 70%,#5b6b3d 100%)}
.strategy-veil{left:0;top:0;width:283px;height:264px;background:rgba(255,255,255,.74)}
.strategy h2{position:absolute;left:0;top:6px;width:283px;font-weight:600;font-size:15.5px}
.strategy .benefits{position:absolute;left:0;top:32px;width:283px}
.burst{left:1106px;top:586px;width:80px;height:80px}
.fine{left:0;top:245px;width:273px;text-align:right;font-style:italic;font-size:5.6px;line-height:8px}

.back-band{left:0;top:264px;width:571px;height:52px;background:var(--navy);color:var(--white)}
.badge-a{left:7px;top:30px;width:35px;height:14px;background:var(--badge);border-radius:2px}
.badge-b{left:47px;top:30px;width:52px;height:14px;background:#3f9a3a;border-radius:2px}
.quote{font-size:13.5px;line-height:18px}
.quote-call{left:103px;top:10px;width:160px}
.quote-or{left:268px;top:18px;width:40px;font-size:15px}
.quote-web{left:312px;top:10px;width:150px}
.brand{left:488px;top:16px;display:flex;align-items:center;gap:4px}
.brand-dot{width:20px;height:20px;border-radius:50%;background:var(--yellow)}
.brand-name{font-weight:700;font-size:10px;color:var(--white)}
</style>
</head>
<body>

<section class="front abs" aria-label="Postcard front">
  <div class="front-photo abs" role="img" aria-label="Moving crew in blue shirts standing in front of branded box trucks"></div>
  <div class="front-notch abs"></div>
  <div class="front-panel abs">
    <p class="front-claim abs center">Over 10,000 in, out and around the Triangle since 1976</p>
    <div class="services abs"><span>LOCAL</span><span>STATEWIDE</span><span>INTERSTATE</span><span>INTERNATIONAL</span><span>STORAGE</span></div>
  </div>
  <h1 class="front-title abs center">Declutter, Sell, Move!</h1>
  <p class="front-sub abs center">...and never lift a finger!</p>
  <div class="front-band abs center">One month free storage for Triangle home sellers<br>(see back for details)</div>
</section>

<section class="back abs" aria-label="Postcard back">
  <div class="plan abs center">
    <h2>Stage your home with staged moving</h2>
    <ul class="benefits">
      <li>Sell your home more quickly</li>
      <li>Increase selling price</li>
      <li>Keep everything in its place</li>
      <li>Make moving day less stressful</li>
      <li>You don’t need to lift a finger</li>
    </ul>
    <div class="stage1 abs">
      <h3 class="stage-title">Stage 1 - Before the Sale</h3>
      <p class="stage-body">We carefully pack all the contents in your home you aren’t using<br>We securely store it in our climate-controlled storage<br>center until you close on your new home</p>
    </div>
    <div class="stage2 abs">
      <h3 class="stage-title">Stage 2 - After your Home Sells</h3>
      <p class="stage-body loose">We will coordinate delivery of both stored contents<br>and moving day contents to your new home, with everything<br>in the proper room! We will even unpack it for you!</p>
    </div>
  </div>

  <div class="strategy abs center">
    <div class="strategy-photo abs" role="img" aria-label="Moving truck parked on a leafy residential driveway"></div>
    <div class="strategy-veil abs"></div>
    <h2>Smarter moving strategies since 1976</h2>
    <ul class="benefits">
      <li>Over 10,000 successful moves since 1976</li>
      <li>Move damage claims 51.5% less than industry average</li>
      <li>Professional trained and tenured staff</li>
      <li>Solutions for unique moving and logistics needs</li>
      <li>Fully liscensed and insured</li>
    </ul>
    <p class="fine abs">*One month free controlled climate storage when using our Staged Moving &amp; Storage Plan.<br>Price will be deducted from final move cost. Not applicable with any other discounts.</p>
  </div>

  <div class="back-band abs">
    <div class="badge-a abs"></div>
    <div class="badge-b abs"></div>
    <p class="quote quote-call abs center">Call for an in-home quote<br>919.555.0148</p>
    <p class="quote quote-or abs center">OR</p>
    <p class="quote quote-web abs center">Quote your move online<br>pellwickmovers.com</p>
    <div class="brand abs"><span class="brand-dot"></span><span class="brand-name">Pellwick Movers</span></div>
  </div>
</section>

<svg class="burst abs" viewBox="0 0 80 80" aria-label="1 Month Storage Free offer">
  <polygon fill="var(--yellow)" points="80,40 73.4,46.6 77,55.3 68.3,58.9 68.3,68.3 58.9,68.3 55.3,77 46.6,73.4 40,80 33.4,73.4 24.7,77 21.1,68.3 11.7,68.3 11.7,58.9 3,55.3 6.6,46.6 0,40 6.6,33.4 3,24.7 11.7,21.1 11.7,11.7 21.1,11.7 24.7,3 33.4,6.6 40,0 46.6,6.6 55.3,3 58.9,11.7 68.3,11.7 68.3,21.1 77,24.7 73.4,33.4"/>
  <g transform="rotate(15 40 40)" fill="var(--navy)" font-family="Ubuntu, sans-serif" text-anchor="middle">
    <text x="40" y="29" font-size="10" font-weight="700">1 Month</text>
    <text x="40" y="40" font-size="10" font-weight="700">Storage Free</text>
    <text x="40" y="50" font-size="5" font-weight="500">*with staged moving</text>
    <text x="40" y="56" font-size="5" font-weight="500">and storage</text>
    <text x="40" y="62" font-size="5" font-style="italic">Expires 12/31/19</text>
  </g>
</svg>

</body>
</html>
```